Lantern Hill Publicity is a new boutique Press Office with a small roster of well-chosen clients across an array of disciplines; from Art and Technology to Restaurants and Fashion. Based in Greenpoint Brooklyn, Lantern Hill Publicity achieves outstanding results through hard work, tenacity, efficiency and a sense of humor. We need a simple, versatile and classic design. We would like each side of the card to be white text on a black background.

Boutique

```html
<!DOCTYPE html>
<html lang="en">
<head>
<meta charset="utf-8">
<title>Lantern Hill Publicity — Business Card</title>
<link rel="stylesheet" href="https://fonts.googleapis.com/css2?family=Playfair+Display:wght@400&family=Montserrat:wght@400&display=swap">
<style>
  :root {
    --stage-bg: #d9d9d9;
    --card-black: #141517;
    --card-ink: #ffffff;
    --card-ink-soft: #d8d8d8;
    --card-shadow: rgba(0, 0, 0, 0.18);
  }
  * { box-sizing: border-box; margin: 0; padding: 0; }
  html, body {
    width: 1200px;
    height: 800px;
    overflow: hidden;
  }
  body {
    background: var(--stage-bg);
    display: flex;
    align-items: center;
    justify-content: center;
    gap: 40px;
  }
  .card {
    position: relative;
    width: 520px;
    height: 297px;
    background: var(--card-black);
    color: var(--card-ink);
    box-shadow: 0 10px 24px var(--card-shadow);
  }

  /* Front: company name */
  .card--front {
    display: flex;
    align-items: center;
    justify-content: center;
  }
  .brand-name {
    font-family: "Playfair Display", serif;
    font-weight: 400;
    font-size: 19px;
    letter-spacing: 0.22em;
    text-transform: uppercase;
    text-align: center;
    line-height: 1.5;
  }

  /* Back: person and contact */
  .card--back { padding: 26px 30px; }
  .person-name {
    font-family: "Playfair Display", serif;
    font-weight: 400;
    font-size: 32px;
    line-height: 1;
  }
  .contact-list {
    position: absolute;
    left: 30px;
    top: 132px;
    list-style: none;
    font-family: "Montserrat", sans-serif;
    font-size: 8.5px;
    letter-spacing: 0.04em;
    color: var(--card-ink-soft);
    text-transform: uppercase;
  }
  .contact-item {
    display: flex;
    align-items: flex-start;
    gap: 10px;
    margin-bottom: 9px;
    line-height: 1.45;
  }
  .contact-icon {
    width: 11px;
    height: 11px;
    flex: none;
    margin-top: 1px;
    fill: var(--card-ink);
  }
</style>
</head>
<body>

  <section class="card card--front" aria-label="Card front">
    <h1 class="brand-name">Lantern Hill<br>Publicity</h1>
  </section>

  <section class="card card--back" aria-label="Card back">
    <h2 class="person-name">Name Lname</h2>
    <ul class="contact-list">
      <li class="contact-item">
        <svg class="contact-icon" viewBox="0 0 12 12" aria-hidden="true">
          <path d="M1 2.5h10v7H1z M1.6 3.1 6 6.6l4.4-3.5" fill="none" stroke="#fff" stroke-width="1.1"/>
        </svg>
        <span>info@companyname.com</span>
      </li>
      <li class="contact-item">
        <svg class="contact-icon" viewBox="0 0 12 12" aria-hidden="true">
          <path d="M3 1 4.8 3.6 3.8 4.8c.6 1.4 1.9 2.8 3.4 3.4l1.2-1L11 9l-1 2C5.3 11 1 6.7 1 2z"/>
        </svg>
        <span>+00 1234 5678 9012<br>+00 1234 5678 9012</span>
      </li>
      <li class="contact-item">
        <svg class="contact-icon" viewBox="0 0 12 12" aria-hidden="true">
          <circle cx="6" cy="6" r="4.8" fill="none" stroke="#fff" stroke-width="1.1"/>
          <path d="M1.2 6h9.6M6 1.2c-2.4 2.6-2.4 7 0 9.6M6 1.2c2.4 2.6 2.4 7 0 9.6" fill="none" stroke="#fff" stroke-width="0.9"/>
        </svg>
        <span>www.company-name.com</span>
      </li>
      <li class="contact-item">
        <svg class="contact-icon" viewBox="0 0 12 12" aria-hidden="true">
          <path d="M6 1 11 5.6H9.5V11H7.2V7.8H4.8V11H2.5V5.6H1z"/>
        </svg>
        <span>Your City Address<br>Street Location, NY City, USA</span>
      </li>
    </ul>
  </section>

</body>
</html>
```